Packaging design for Prenatal, Fish Oil, and Joint Pain product

We are looking for package design (label and outer box) for following products:
1) Moreval
- Product name: Moreval
- Benefit: Prenatal
- Feature DHA + Folic Acid
- What we need from you? We need box concept
- Box dimension 55mm Height x 145mm length x 100mm width
2) Omega 3 Alaskan Salmon
- Product name: Omega 3 Alaskan Salmon
- Benefit: Cognitive , cardiovascular Health, Joint Health, High cholesterol
- Feature: Alaskan Salmon
- What we need from you? We need label concept
- Label dimension: 60mm Height x 180mm Length
2) Quorba
- Product name: Quorba
- Benefit: Joint Health
- Feature: Glucosamin, Chondroitin, MSM
Designer can use generic text on other vitamin products for formula, usage instruction etc.
We have logo. The logo must be integrated in the packaging design. (please see attachment)

```html
<!DOCTYPE html>
<html lang="en">
<head>
<meta charset="utf-8">
<title>Omega 3 Wild Salmon Oil – Box Panels</title>
<link rel="stylesheet" href="https://fonts.googleapis.com/css2?family=Alfa+Slab+One&family=Libre+Baskerville:wght@400;700&family=Arimo:wght@400;700&display=swap">
<style>
  :root{
    --bg:#e6e6e6;
    --yellow:#fff200;
    --yellow-soft:#f7f46a;
    --navy:#1b2f6b;
    --navy-deep:#13224f;
    --sky:#1a93d1;
    --red:#d8262d;
    --ink:#222;
    --rule:#b9b06a;
    --paper:#ffffff;
    --grey-panel:#f2f2f2;
  }
  *{box-sizing:border-box;margin:0;padding:0}
  html,body{width:1200px;height:900px;overflow:hidden}
  body{background:var(--bg);position:relative;font-family:"Arimo",Arial,sans-serif;color:var(--ink)}
  .box{position:absolute;top:130px;left:220px;width:760px;height:640px;display:flex;box-shadow:0 20px 40px rgba(0,0,0,.18)}
  .panel{position:relative;height:100%;overflow:hidden}
  .panel--side{width:320px;background:var(--yellow)}
  .panel--front{width:440px;background:var(--yellow)}

  .brand{font-family:"Libre Baskerville",Georgia,serif;font-weight:700;color:var(--red);display:flex;align-items:center;gap:6px;justify-content:center}
  .brand__dot{width:8px;height:8px;border-radius:50%;background:var(--red)}
  .title-lockup{position:relative;display:inline-block}
  .rich-in{position:absolute;top:0;left:0;font-family:"Libre Baskerville",Georgia,serif;font-weight:700;color:var(--navy);white-space:nowrap;transform:rotate(-10deg);transform-origin:left bottom}
  .omega{font-family:"Alfa Slab One",Georgia,serif;color:var(--navy);line-height:1}
  .omega sup{font-size:.5em;vertical-align:.55em}
  .dose{display:block;text-align:center;font-family:"Libre Baskerville",Georgia,serif;font-weight:700;color:var(--navy)}

  /* side panel */
  .side-head{position:absolute;top:22px;left:0;right:0;text-align:center}
  .side-head .brand{font-size:18px}
  .side-head .title-lockup{padding-top:16px}
  .side-head .rich-in{font-size:10px;left:-8px}
  .side-head .omega{font-size:44px}
  .side-head .dose{font-size:10px;margin-top:-2px}
  .side-rule{position:absolute;top:140px;left:40px;right:40px;height:1px;background:var(--rule)}
  .side-title{position:absolute;top:152px;left:0;right:0;text-align:center;font-family:"Libre Baskerville",Georgia,serif;font-weight:700;font-size:18px;color:var(--navy)}
  .facts{position:absolute;top:196px;left:12px;width:180px;background:var(--paper);border:1px solid #888;padding:6px 6px 4px;font-size:6.5px}
  .facts h3{font-size:9px;font-weight:700}
  .facts p{line-height:1.35}
  .facts table{width:100%;border-collapse:collapse;margin-top:4px}
  .facts th{font-weight:400;text-align:right;font-size:5.5px;border-bottom:2px solid #555;padding:2px 0}
  .facts td{border-bottom:1px solid #bbb;padding:3px 0}
  .facts td:nth-child(2),.facts td:nth-child(3){text-align:right}
  .facts .indent{padding-left:8px}
  .facts .note{font-size:5.5px;margin-top:4px}
  .info{position:absolute;top:400px;left:12px;right:12px;height:200px;background:var(--grey-panel);padding:8px;font-size:6.8px;line-height:1.5}
  .info p{margin-bottom:6px}
  .info b{font-weight:700}
  .side-base{position:absolute;bottom:0;left:0;right:0;height:34px;background:var(--sky)}

  /* front panel */
  .sunburst{position:absolute;inset:0 0 auto 0;height:380px;background:radial-gradient(circle at 50% 72%,#fffbd0 0,var(--yellow) 30%,var(--yellow-soft) 70%,var(--yellow) 100%)}
  .front-head{position:absolute;top:40px;left:0;right:0;text-align:center}
  .front-head .brand{font-size:26px}
  .front-head .title-lockup{padding-top:22px;margin-top:2px}
  .front-head .rich-in{font-size:14px;left:-10px}
  .front-head .omega{font-size:70px;text-shadow:2px 2px 0 #fff,-2px -2px 0 #fff,2px -2px 0 #fff,-2px 2px 0 #fff}
  .front-head .dose{font-size:14px;margin-top:2px}
  .scene-art{position:absolute;top:250px;left:0;width:440px;height:150px}
  .front-band{position:absolute;top:380px;left:0;right:0;height:210px;background:linear-gradient(180deg,var(--navy) 0,var(--navy-deep) 100%)}
  .front-title{position:absolute;top:412px;left:0;right:0;text-align:center;font-family:"Libre Baskerville",Georgia,serif;font-weight:700;font-size:27px;color:#fff}
  .front-rule{position:absolute;top:458px;left:90px;right:90px;height:2px;background:#b8c23a}
  .front-sub{position:absolute;top:470px;left:0;right:0;text-align:center;font-family:"Libre Baskerville",Georgia,serif;font-weight:700;font-size:17px;color:#fff}
  .count{position:absolute;top:508px;right:24px;width:90px;text-align:center}
  .count__disc{width:58px;height:58px;margin:0 auto;border-radius:50%;background:#fff;border:5px solid var(--sky);display:flex;align-items:center;justify-content:center;font-family:"Libre Baskerville",Georgia,serif;font-weight:700;font-size:20px;color:var(--navy)}
  .count__label{font-family:"Libre Baskerville",Georgia,serif;font-weight:700;font-size:10px;color:#fff;margin-top:2px}
  .front-base{position:absolute;bottom:0;left:0;right:0;height:50px;background:var(--sky)}
</style>
</head>
<body>
<main class="box">
  <section class="panel panel--side">
    <header class="side-head">
      <div class="brand"><span class="brand__dot"></span>Velora</div>
      <div class="title-lockup">
        <span class="rich-in">Rich in</span>
        <div class="omega">Omega<sup>3</sup></div>
        <span class="dose">1000mg</span>
      </div>
    </header>
    <div class="side-rule"></div>
    <h2 class="side-title">Wild Salmon Oil</h2>

    <div class="facts">
      <h3>Supplement Facts</h3>
      <p>Serving Size: 2 Softgels<br>Servings per Container: 90</p>
      <table>
        <tr><th></th><th>Amount Per Serving</th><th>% Daily Value</th></tr>
        <tr><td>Calories</td><td>18</td><td></td></tr>
        <tr><td class="indent">Calories from Fat</td><td>18</td><td></td></tr>
        <tr><td>Total Fat</td><td>2g</td><td>3%†</td></tr>
        <tr><td>Vitamin E (from mixed natural tocopherols)</td><td>4 IU</td><td>13%</td></tr>
        <tr><td>Purified Fish Oil (molecularly distilled)</td><td>2g</td><td>*</td></tr>
        <tr><td class="indent">EPA (eicosapentaenoic acid)</td><td>360mg</td><td>*</td></tr>
        <tr><td class="indent">DHA (docosahexaenoic acid)</td><td>240mg</td><td>*</td></tr>
      </table>
      <p class="note">†Percent Daily Values are based on a 2,000 calorie diet.<br>*Daily value not established.</p>
    </div>

    <div class="info">
      <p><b>Other Ingredients:</b> Gelatin, Purified Water, Glycerin and Natural Lemon Oil.</p>
      <p><b>Contains:</b> Fish (Sardine, Mackerel, Anchovy).</p>
      <p><b>Directions:</b> For adults take two (2) softgels daily as a dietary supplement with meal. If you are pregnant, nursing, taking any medications, or planning any medical procedure, consult your doctor before use. Discontinue use and consult your doctor if any adverse reactions occur.</p>
      <p><b>Storage Instruction:</b> Keep out of reach of children. Store in a cool, dry place. Do not use if seal under cap is broken or missing.</p>
    </div>
    <div class="side-base"></div>
  </section>

  <section class="panel panel--front">
    <div class="sunburst"></div>
    <header class="front-head">
      <div class="brand"><span class="brand__dot"></span>Velora</div>
      <div class="title-lockup">
        <span class="rich-in">Rich in</span>
        <div class="omega">Omega<sup>3</sup></div>
        <span class="dose">1000mg</span>
      </div>
    </header>
    <svg class="scene-art" viewBox="0 0 440 150" role="img" aria-label="Illustration of a rising sun behind icebergs with a wild salmon leaping over the sea">
      <defs>
        <linearGradient id="sceneTone" x1="0" y1="0" x2="0" y2="1">
          <stop offset="0" stop-color="#fff6a0"/>
          <stop offset="0.55" stop-color="#d9ecf5"/>
          <stop offset="1" stop-color="#7fa6bf"/>
        </linearGradient>
      </defs>
      <rect x="0" y="0" width="440" height="150" fill="url(#sceneTone)" opacity="0.85"/>
    </svg>
    <div class="front-band"></div>
    <h1 class="front-title">Wild Salmon Oil</h1>
    <div class="front-rule"></div>
    <p class="front-sub">Dietary Supplement</p>
    <div class="count">
      <div class="count__disc">180</div>
      <div class="count__label">Softgels</div>
    </div>
    <div class="front-base"></div>
  </section>
</main>
</body>
</html>
```